Deactivated Coal-Fired Power Plant to be redeveloped into a Green Energy Campus.

Want a striking business card statement that introduces our concept project to provide economic and community recovery to a former rural coal community in western PA.
Essentially 12 project representatives that will lead both the demolition of an existing power plant and the redevelopment to a new Green energy site.
Business Card should reflect our effort.
We are open to ideas.

Target Market(s)

Energy and Power Generation industries

Industry/Entity Type

Power Generation and Data Centers

Contact Information for Business Card

Included in uploaded materials

Font styles to use
Sans Serif
Other font styles liked:
• Arial, Calibri

Requirements
Must have
• Multiple colors

```html
<!DOCTYPE html>
<html lang="en">
<head>
<meta charset="utf-8">
<title>Ridgeline Renewal – Business Card</title>
<link rel="stylesheet" href="https://fonts.googleapis.com/css2?family=Outfit:wght@400;600&display=swap">
<style>
  :root {
    --stage: #6f6f71;
    --card: #ffffff;
    --green: #11974a;
    --ink: #111111;
    --text: #222222;
    --photo-sky: #b9c3c9;
    --photo-land: #3f5a34;
    --photo-deep: #24361f;
  }
  * { margin: 0; padding: 0; box-sizing: border-box; }
  html, body {
    width: 1200px; height: 1200px; overflow: hidden;
    background: var(--stage);
    font-family: "Outfit", Arial, sans-serif;
  }
  .card {
    position: absolute; left: 307px; width: 585px; height: 357px;
    border-radius: 18px; overflow: hidden; background: var(--card);
  }
  .card--front { top: 222px; }
  .card--back { top: 677px; }
  .card__band {
    position: absolute; left: 0; right: 0; bottom: 0; height: 22px;
    background: var(--green);
  }
  .brand {
    position: absolute; display: flex; align-items: center; gap: 10px;
    font-weight: 600; white-space: nowrap; letter-spacing: 0.5px;
  }
  .brand__dot { border-radius: 50%; flex: none; }
  .card--front .brand { left: 42px; top: 52px; font-size: 28px; color: var(--ink); }
  .card--front .brand__dot { width: 26px; height: 26px; background: var(--green); }
  .front-art { position: absolute; left: 0; top: 0; }
  .contact-tab {
    position: absolute; left: 0; top: 214px; width: 13px; height: 32px;
    background: var(--green);
  }
  .person { position: absolute; left: 42px; top: 208px; }
  .person__name { font-size: 21px; font-weight: 600; color: var(--green); letter-spacing: 0.3px; }
  .person__title { font-size: 14px; color: var(--text); margin-top: 2px; letter-spacing: 0.3px; }
  .contacts { position: absolute; left: 42px; top: 275px; list-style: none; }
  .contacts li {
    display: flex; align-items: center; gap: 6px;
    font-size: 13.5px; color: var(--text); height: 21px; letter-spacing: 0.2px;
  }
  .contacts svg { width: 14px; height: 14px; flex: none; }
  .back-photo {
    position: absolute; left: 0; top: 0; width: 100%; height: 335px;
    background: linear-gradient(180deg, var(--photo-sky) 0%, #8a968f 18%, var(--photo-land) 35%, #4d6a3c 65%, var(--photo-deep) 100%);
  }
  .card--back .brand {
    left: 50%; top: 220px; transform: translateX(-50%);
    font-size: 34px; color: #ffffff;
  }
  .card--back .brand__dot { width: 30px; height: 30px; background: #ffffff; }
</style>
</head>
<body>
  <section class="card card--front">
    <svg class="front-art" width="585" height="357" viewBox="0 0 585 357" role="img" aria-label="Decorative brand illustration area">
      <circle cx="598" cy="330" r="255" fill="var(--green)"/>
    </svg>
    <div class="brand"><span>Ridgeline Renewal</span><span class="brand__dot"></span></div>
    <div class="contact-tab"></div>
    <div class="person">
      <p class="person__name">Daniel Okafor</p>
      <p class="person__title">Chief Operating Officer</p>
    </div>
    <ul class="contacts">
      <li>
        <svg viewBox="0 0 14 14"><rect width="14" height="14" fill="var(--green)"/><path d="M4 3.2l1.6 1.8-.8 1.1c.6 1.2 1.5 2.1 2.7 2.7l1.1-.8 1.8 1.6-1 1.3C6.6 10.6 3.4 7.4 2.7 4.2z" fill="#fff"/></svg>
        555-014-2200
      </li>
      <li>
        <svg viewBox="0 0 14 14"><rect width="14" height="14" fill="var(--green)"/><rect x="3" y="4.3" width="8" height="5.6" fill="none" stroke="#fff" stroke-width="1"/><path d="M3 4.5l4 3 4-3" fill="none" stroke="#fff" stroke-width="1"/></svg>
        dokafor@ridgelinerenewal.com
      </li>
    </ul>
    <div class="card__band"></div>
  </section>

  <section class="card card--back">
    <div class="back-photo" role="img" aria-label="Aerial photograph of the power plant site in green rolling countryside"></div>
    <div class="brand"><span>Ridgeline Renewal</span><span class="brand__dot"></span></div>
    <div class="card__band"></div>
  </section>
</body>
</html>
```